Commercial Janitorial Company needs a Postcard Design

We need a postcard design-i attached a sample-of one-not our industry-but same size and similar to content and what i am looking for-We are a commercial janitorial service-(not residential) we service High Tech-Bio Tech-Manufacturing-Office-Property Management Company'sThe design should incorporate Industry Services-Industries served website-company information-Two sided-color-our website: www.tidewellfacilitysvc.com will have information to use-bullet point type-should include Nice artwork-Attention grabbing headline then of course all our contact information found on website

The postcard is NOT a mailer but a hand-out (2 sides)-about 9" Long by 7" wide-

Target Market(s)

Commercial office Building's

Colors

Designer to choose colors to be used in the design.

Requirements
Must have
• All company information-website
• Services offered-Industries served
• Something mentioned about "Green Cleaning"
• Images of cleaning are good-in a commercial setting--Hi Tech-Bio Tech-Cleanroom Cleaning
• 24/7 access
• Locally owned and operated
• 25 Years in business
• Service Excellence
• With our highly-trained, in-house workforce, you can trust that we’ll provide you with services that increase efficiencies and lower your operating expenses—all while maintaining a uniform standard of service excellence.
• Breadth of Services
• We’ll provide you with an unrivaled range of facilities solutions that will keep your properties safe, clean, comfortable and energy efficient.
• Technology-Enabled Workforce
• Your facilities will be serviced with the support of innovative technology solutions that will simplify service delivery and allow for greater transparency.
• Guaranteed Sustainability Solutions
• We’ve got expertise to support all of your sustainability goals, including green cleaning, KOBA support, bundled energy solutions, and more.
• Size of Postcard is 9.5" length x 7" width
Should not have
• No Residential
• No Maid service
• No Cartoon type images
• Strickly commercial cleaning

```html
<!DOCTYPE html>
<html lang="en">
<head>
<meta charset="utf-8">
<title>Tidewell Facility Services – Postcard Front</title>
<link href="https://fonts.googleapis.com/css2?family=Roboto+Condensed:wght@700&family=Arimo:wght@700&display=swap" rel="stylesheet">
<style>
  :root {
    --backdrop: #4a4848;
    --card-white: #ffffff;
    --ink: #111111;
    --band-black: #000000;
    --brand-blue: #1b7cc4;
    --brand-blue-dark: #0f5fa3;
    --accent-yellow: #f4d21c;
  }
  * { margin: 0; padding: 0; box-sizing: border-box; }
  html, body { width: 1200px; height: 943px; overflow: hidden; }
  body { background: var(--backdrop); position: relative; font-family: "Arimo", Arial, sans-serif; }

  .postcard {
    position: absolute; left: 110px; top: 90px;
    width: 980px; height: 762px;
    background: var(--card-white); overflow: hidden;
  }
  .photo { position: absolute; }
  .photo-mopping {
    left: 0; top: 0; width: 285px; height: 400px;
    background: linear-gradient(160deg, #9a9c9e 0%, #6f7375 45%, #b9bbbc 100%);
  }
  .photo-cleanroom {
    left: 285px; top: 0; width: 285px; height: 212px;
    background: linear-gradient(135deg, #e7ecef 0%, #c9d2d8 55%, #8d969b 100%);
  }
  .photo-floor-care {
    left: 0; top: 400px; width: 570px; height: 315px;
    background: linear-gradient(120deg, #d9c24a 0%, #a9b3b8 35%, #7f8a90 70%, #c7cfd3 100%);
  }

  .sectors-list {
    position: absolute; left: 598px; top: 42px; list-style: none;
  }
  .sectors-list li {
    position: relative; padding-left: 25px;
    font-size: 18px; line-height: 26px; color: var(--ink);
    text-transform: uppercase; letter-spacing: 0.2px;
  }
  .sectors-list li::before {
    content: ""; position: absolute; left: 2px; top: 8px;
    width: 9px; height: 9px; background: var(--brand-blue);
  }

  .headline-band {
    position: absolute; left: 285px; top: 212px; width: 695px; height: 188px;
    background: var(--band-black); text-align: center; color: var(--card-white);
  }
  .headline {
    font-family: "Roboto Condensed", "Arial Narrow", sans-serif;
    font-size: 52px; line-height: 56px; padding-top: 24px; letter-spacing: -0.3px;
  }
  .headline .highlight { color: var(--brand-blue); }
  .tagline {
    margin-top: 8px; font-size: 18px; color: var(--brand-blue);
  }

  .contact-panel {
    position: absolute; left: 570px; top: 400px; width: 410px; height: 315px;
    text-align: center;
  }
  .company-name {
    position: absolute; left: 60px; top: 48px; width: 300px;
    display: flex; align-items: center; gap: 14px;
  }
  .company-name .mark {
    flex: none; width: 40px; height: 40px; background: var(--brand-blue);
  }
  .company-name .name-text {
    font-family: "Roboto Condensed", "Arial Narrow", sans-serif;
    font-size: 34px; line-height: 36px; color: var(--brand-blue);
    text-align: left;
  }
  .phone {
    position: absolute; left: 0; top: 218px; width: 100%;
    font-family: "Roboto Condensed", "Arial Narrow", sans-serif;
    font-size: 50px; line-height: 54px; color: var(--ink);
  }
  .website {
    position: absolute; left: 0; top: 278px; width: 100%;
    font-size: 15px; color: var(--brand-blue);
  }

  .benefits-bar {
    position: absolute; left: 0; top: 715px; width: 980px; height: 47px;
    background: linear-gradient(180deg, var(--brand-blue) 0%, var(--brand-blue-dark) 100%);
    display: flex; justify-content: center; align-items: center; gap: 12px;
    color: var(--card-white); font-size: 17px; text-transform: uppercase;
  }
  .benefits-bar .divider {
    width: 3px; height: 18px; background: var(--accent-yellow);
  }
</style>
</head>
<body>
  <main class="postcard">
    <div class="photo photo-mopping" role="img" aria-label="Worker in red protective suit squeegeeing a metal floor in an industrial storage room"></div>
    <div class="photo photo-cleanroom" role="img" aria-label="Technician in white cleanroom suit cleaning equipment in a lab"></div>

    <ul class="sectors-list">
      <li>High Technology</li>
      <li>Corporate Office Buildings</li>
      <li>Bio Tech/Pharma</li>
      <li>Manufacturing</li>
      <li>Gov/ Defense</li>
      <li>Educational</li>
    </ul>

    <section class="headline-band">
      <h1 class="headline">Expert <span class="highlight">Commercial Cleaning</span><br>Services In All Sectors</h1>
      <p class="tagline">25 years serving San Jose and the surrounding areas</p>
    </section>

    <div class="photo photo-floor-care" role="img" aria-label="Yellow wet floor caution signs beside a floor polishing machine on a shiny wet floor"></div>

    <section class="contact-panel">
      <div class="company-name">
        <span class="mark"></span>
        <span class="name-text">TIDEWELL FACILITY SERVICES INC.</span>
      </div>
      <p class="phone">408-555-0172</p>
      <p class="website">www.tidewellfacilitysvc.com</p>
    </section>

    <footer class="benefits-bar">
      <span>24/7 Access</span>
      <span class="divider"></span>
      <span>Locally Owned and Operated</span>
      <span class="divider"></span>
      <span>Non Toxic Eco Friendly Solutions</span>
    </footer>
  </main>
</body>
</html>
```